Velumor Business Card Design Project

Need a design for Velumor business cards
Square rounded corner card:
http://www.printquarry.example/25-X-25-Rounded-Corner-Business-Cards_p_204.html
Front content (specific example is used to establish format):
Toby Harlow
Founder
415-287-3391
toby@velumor.example
@tobyjharlow
www.velumor.example
Back content:
Vertical velumor logo (white on red)
https://files.example.net/sh/qz4kxw7rbnle31p/AAKuwd3P571Hr0mLc2sYeqTB9a?dl=0
Target Market(s)
Young professionals (early 20's)
Industry/Entity Type
Business
Requirements
Must have
- Look similar to
http://cdn.artlobby.example/design_img/391846/52310/52310_8162093_391846_image.jpg
Adapted to square rounded corner format

```html
<!DOCTYPE html>
<html lang="en">
<head>
<meta charset="utf-8">
<title>Velumor Business Cards</title>
<link rel="stylesheet" href="https://fonts.googleapis.com/css2?family=Montserrat:wght@300;500&display=swap">
<style>
  :root {
    --backdrop: #dedede;
    --card-red: #d9261d;
    --ink-white: #ffffff;
  }
  html, body {
    margin: 0;
    padding: 0;
    width: 1200px;
    height: 875px;
    overflow: hidden;
    background: var(--backdrop);
  }
  .canvas {
    position: relative;
    width: 1200px;
    height: 875px;
  }
  .card {
    position: absolute;
    top: 245px;
    width: 386px;
    height: 384px;
    border-radius: 17px;
    background: var(--card-red);
    color: var(--ink-white);
    font-family: "Montserrat", sans-serif;
  }
  .card--front { left: 190px; }
  .card--back { left: 624px; }

  .brand-row {
    position: absolute;
    top: 54px;
    left: 56px;
    display: flex;
    align-items: center;
    gap: 16px;
  }
  .brand-mark {
    width: 46px;
    height: 46px;
    background: var(--ink-white);
    border-radius: 4px;
  }
  .brand-name {
    font-weight: 500;
    font-size: 44px;
    line-height: 1;
    letter-spacing: 1px;
  }

  .contact {
    position: absolute;
    top: 170px;
    left: 0;
    width: 100%;
    text-align: center;
    font-weight: 300;
    font-size: 19px;
    line-height: 26px;
  }
  .contact p { margin: 0; }
  .contact .person { margin-bottom: 24px; }

  .back-lockup {
    position: absolute;
    inset: 0;
    display: flex;
    flex-direction: column;
    align-items: center;
    justify-content: center;
    gap: 30px;
  }
  .back-lockup .brand-name {
    font-size: 50px;
  }
  .back-lockup .brand-mark {
    width: 90px;
    height: 90px;
    border-radius: 50%;
  }
</style>
</head>
<body>
<main class="canvas">
  <section class="card card--front">
    <div class="brand-row">
      <div class="brand-mark"></div>
      <span class="brand-name">velumor</span>
    </div>
    <div class="contact">
      <div class="person">
        <p class="contact-name">Toby Harlow</p>
        <p class="contact-role">founder</p>
      </div>
      <p class="contact-phone">415-287-3391</p>
      <p class="contact-email">toby@velumor.example</p>
      <p class="contact-handle">@tobyjharlow</p>
      <p class="contact-web">www.velumor.example</p>
    </div>
  </section>

  <section class="card card--back">
    <div class="back-lockup">
      <span class="brand-name">velumor</span>
      <div class="brand-mark"></div>
    </div>
  </section>
</main>
</body>
</html>
```